business card for an electronic retail store

take our existing color logo, design a new business card and make a black&white version of the logo as well

Industry/Entity Type

Electronic

```html
<!DOCTYPE html>
<html lang="en">
<head>
<meta charset="utf-8">
<title>Voltline Business Card</title>
<link href="https://fonts.googleapis.com/css2?family=Michroma&family=Tinos&display=swap" rel="stylesheet">
<style>
  :root {
    --bg: #d9d6d1;
    --card-black: #0d0d0d;
    --card-yellow: #f7d21a;
    --accent-red: #c8161d;
    --brand-yellow: #f6d11b;
    --text-light: #f2f2f2;
    --text-dark: #3a3a3a;
    --icon-dark: #2c2c2c;
  }
  * { margin: 0; padding: 0; box-sizing: border-box; }
  html, body {
    width: 1200px; height: 899px; overflow: hidden;
    background: var(--bg);
  }
  .card {
    position: absolute; left: 100px; top: 160px;
    width: 1000px; height: 580px;
    border-radius: 44px; overflow: hidden;
    background: var(--card-yellow);
    box-shadow: 0 14px 34px rgba(0,0,0,0.22);
  }
  .card-bands { position: absolute; inset: 0; }
  .brand {
    position: absolute; left: 92px; top: 74px;
    display: flex; align-items: center; gap: 16px;
  }
  .brand-square {
    width: 40px; height: 40px; background: var(--accent-red);
  }
  .brand-name {
    font-family: "Michroma", sans-serif;
    font-size: 52px; color: var(--brand-yellow);
    letter-spacing: 1px; line-height: 1;
  }
  .tagline {
    position: absolute; left: 94px; top: 144px;
    font-family: "Tinos", serif; font-size: 27px;
    color: var(--text-light); letter-spacing: 0.5px;
  }
  .contact {
    position: absolute; left: 60px; top: 360px;
    display: flex; font-family: "Michroma", sans-serif;
    color: var(--text-dark); text-transform: uppercase;
  }
  .contact-person {
    width: 420px; text-align: right; padding-right: 20px;
    font-size: 17px; line-height: 30px;
  }
  .person-name { font-size: 19px; }
  .person-address { margin-top: 8px; }
  .contact-divider { width: 2px; background: var(--text-dark); height: 176px; }
  .contact-lines {
    padding-left: 16px; font-size: 17px; line-height: 30px;
    list-style: none;
  }
  .contact-lines li { display: flex; align-items: center; gap: 10px; }
  .contact-icon { width: 18px; height: 18px; flex: none; }
</style>
</head>
<body>
  <div class="card">
    <svg class="card-bands" viewBox="0 0 1000 580" width="1000" height="580" aria-hidden="true">
      <path d="M0,0 H1000 V404 C800,330 480,262 0,228 Z" fill="var(--card-black)"/>
      <path d="M0,228 C480,262 800,330 1000,404 V432 C800,352 460,282 0,246 Z" fill="var(--accent-red)"/>
    </svg>

    <div class="brand">
      <span class="brand-square"></span>
      <span class="brand-name">VOLTLINE</span>
    </div>
    <p class="tagline">Car Audio · Performance · Security</p>

    <div class="contact">
      <div class="contact-person">
        <p class="person-name">Mark Ellison</p>
        <p class="person-title">Owner / C.E.O</p>
        <p class="person-address">Suite # 118, Kern Bldg,<br>NY 40712</p>
      </div>
      <div class="contact-divider"></div>
      <ul class="contact-lines">
        <li><svg class="contact-icon" viewBox="0 0 18 18"><circle cx="9" cy="9" r="9" fill="var(--icon-dark)"/><path d="M6 4.5l2 2-1 1.2c.6 1.3 1.6 2.3 2.8 2.8l1.2-1 2 2-1.2 1.5C8.6 12.8 5.2 9.4 4.5 6z" fill="var(--card-yellow)"/></svg>555-210-4471</li>
        <li><svg class="contact-icon" viewBox="0 0 18 18"><circle cx="9" cy="9" r="9" fill="var(--icon-dark)"/><rect x="6" y="3.5" width="6" height="11" rx="1.2" fill="var(--card-yellow)"/></svg>555-308-9124</li>
        <li><svg class="contact-icon" viewBox="0 0 18 18"><circle cx="9" cy="9" r="9" fill="var(--icon-dark)"/><rect x="4.5" y="7" width="9" height="6" fill="var(--card-yellow)"/><rect x="6" y="4" width="6" height="3" fill="var(--card-yellow)"/></svg>555-647-2058</li>
        <li><svg class="contact-icon" viewBox="0 0 18 18"><circle cx="9" cy="9" r="9" fill="var(--icon-dark)"/><rect x="4" y="5.5" width="10" height="7" fill="var(--card-yellow)"/><path d="M4 5.5l5 4 5-4" fill="none" stroke="var(--icon-dark)" stroke-width="1.2"/></svg>mark@voltlineaudio.com</li>
        <li><svg class="contact-icon" viewBox="0 0 18 18"><circle cx="9" cy="9" r="9" fill="var(--icon-dark)"/><circle cx="9" cy="9" r="5" fill="none" stroke="var(--card-yellow)" stroke-width="1.3"/><path d="M4 9h10M9 4v10" stroke="var(--card-yellow)" stroke-width="1.1"/></svg>www.voltlineaudio.com</li>
      </ul>
    </div>
  </div>
</body>
</html>
```